Challenge Graphics for Social Media

I want to create 9 social media graphics (new Instagram size 4:5 (1080 x 1350 pixels) focusing on our next 12-Week Amber Broth Quest on May 4th. Use any of the pics in the dropbox, NO RANDOM STOCK PHOTOGRAPHY. For the color scheme of the graphics, they should all be complementary to the green smoothie book attached.
You should add a copy of the book AND a bottle of the green smoothie gummies to each graphic. Note: all the pics from the dropbox are also attached here. The text for these graphics are one of the 2 options:
Summer is 2 Months Away!
Join the 12-Week Amber Broth Quest on May 4th!
Lose Up to 15lbs in 10 Days!
Get Your Summer Body Ready!
Join the 12-Week Amber Broth Quest (with Gummies)
Begins Monday May 4th

```html
<!DOCTYPE html>
<html lang="en">
<head>
<meta charset="utf-8">
<title>12-Week Amber Broth Quest – Social Graphics</title>
<link href="https://fonts.googleapis.com/css2?family=Lexend:wght@400;600;700&family=Poppins:ital,wght@0,500;0,600;1,600;1,800&display=swap" rel="stylesheet">
<style>
  :root {
    --board: #232a23;
    --green-deep: #0f6410;
    --green-text: #15780f;
    --green-mid: #3b8f34;
    --green-soft: #a9d3a3;
    --green-pale: #d4e9d0;
    --cream: #f4f8f1;
    --white: #ffffff;
    --ink: #1b1b1b;
    --skin-a: #c98f6c;
    --skin-b: #e7a9cf;
    --dots: #2a2a2a;
  }
  * { box-sizing: border-box; margin: 0; padding: 0; }
  html, body { width: 981px; height: 1200px; overflow: hidden; background: var(--board); }
  .board { position: relative; width: 981px; height: 1200px; }
  .card {
    position: absolute; width: 262px; height: 327px; overflow: hidden;
    background: var(--cream); box-shadow: 0 4px 14px rgba(0,0,0,.35);
    font-family: "Lexend", sans-serif;
  }
  .card > svg.bg { position: absolute; inset: 0; width: 262px; height: 327px; }
  .txt { position: absolute; line-height: 1.12; }
  .kicker { font-family: "Poppins", sans-serif; font-weight: 500; font-size: 11px; }
  .headline { font-weight: 700; font-size: 22px; line-height: 1.05; }
  .title { font-weight: 700; font-size: 16px; }
  .title small { font-size: 11.5px; font-weight: 600; }
  .title sup { font-size: 9px; }
  .date { font-family: "Poppins", sans-serif; font-weight: 600; font-size: 11px; line-height: 1.1; }
  .promo { font-family: "Poppins", sans-serif; font-style: italic; font-weight: 600; font-size: 14px; line-height: 1.05; }
  .promo b { font-weight: 800; font-size: 20px; }
  .promo-caps { font-family: "Poppins", sans-serif; font-style: italic; font-weight: 800; font-size: 12px; line-height: 1.05; }
  .promo-caps b { font-size: 19px; }
  .c-white { color: var(--white); }
  .c-green { color: var(--green-text); }
  .c-soft { color: var(--green-soft); }
  .c-ink { color: var(--ink); }
  .c-deep { color: var(--green-deep); }
  .photo {
    position: absolute;
    background: linear-gradient(180deg, var(--skin-a) 0%, #2a2a2a 55%, var(--skin-b) 100%);
    border-radius: 40% 40% 6px 6px;
  }
  .photo.pink { background: linear-gradient(180deg, #2a1d1a 0%, var(--skin-a) 25%, var(--skin-b) 60%, #f0b6d8 100%); }
  .photo.round { border-radius: 50%; border: 6px solid var(--green-soft); }
  .bottle {
    position: absolute; border-radius: 8px 8px 6px 6px;
    background: linear-gradient(180deg, var(--green-mid) 0 12%, #5a3a2c 12% 30%, #f3f3f3 30% 92%, #5a3a2c 92%);
  }
</style>
</head>
<body>
<div class="board">

  <!-- Card 1 -->
  <section class="card" style="left:71px;top:72px;">
    <svg class="bg" viewBox="0 0 262 327" aria-hidden="true">
      <path d="M110 0 C150 40 190 80 262 70 L262 0 Z" fill="var(--green-pale)"/>
      <path d="M0 150 C80 130 130 210 262 170 L262 327 L0 327 Z" fill="var(--green-deep)"/>
      <circle cx="193" cy="240" r="82" fill="none" stroke="var(--green-mid)" stroke-width="10"/>
    </svg>
    <div class="bottle" style="left:196px;top:6px;width:50px;height:100px;" role="img" aria-label="Gummies bottle"></div>
    <p class="txt kicker" style="left:13px;top:54px;color:#6aa86a;">Summer is 2 Months Away!</p>
    <p class="txt title c-green" style="left:13px;top:78px;width:185px;">Join the 12-Week<br>Amber Broth<br>Quest <small>(with Gummies)</small></p>
    <p class="txt date c-soft" style="left:13px;top:186px;">Begins<br>Monday May 4th</p>
    <p class="txt promo c-white" style="left:13px;top:216px;">LOSE UP<br><b>15LBS</b> in<br>10 Days!</p>
    <div class="photo round" style="left:124px;top:171px;width:138px;height:138px;" role="img" aria-label="Smiling coach holding the gummies bottle"></div>
  </section>

  <!-- Card 2 -->
  <section class="card" style="left:358px;top:72px;background:var(--white);">
    <svg class="bg" viewBox="0 0 262 327" aria-hidden="true">
      <path d="M0 0 L262 0 L262 130 C200 200 120 220 0 180 Z" fill="var(--green-deep)"/>
      <path d="M262 130 C220 210 110 230 0 205 L0 180 C120 220 200 200 262 130 Z" fill="var(--green-pale)"/>
      <path d="M170 327 C210 290 240 280 262 270 L262 327 Z" fill="var(--green-pale)"/>
      <circle cx="180" cy="110" r="72" fill="none" stroke="var(--green-mid)" stroke-width="8"/>
    </svg>
    <p class="txt headline c-soft" style="left:17px;top:17px;">Get Your<br>Summer<br>Body<br>Ready!</p>
    <p class="txt promo-caps c-white" style="left:17px;top:126px;">LOSE UP TO<br><b>5LBS</b><br>IN 10 DAYS!</p>
    <div class="photo pink" style="left:130px;top:26px;width:108px;height:152px;" role="img" aria-label="Coach in pink outfit cheering with gummies"></div>
    <div class="bottle" style="left:20px;top:212px;width:52px;height:98px;" role="img" aria-label="Gummies bottle"></div>
    <p class="txt title c-green" style="left:82px;top:220px;width:175px;">Join the 12-Week<br>Amber Broth Quest<br>on May 4<sup>th</sup>!</p>
  </section>

  <!-- Card 3 -->
  <section class="card" style="left:644px;top:72px;">
    <svg class="bg" viewBox="0 0 262 327" aria-hidden="true">
      <path d="M0 0 L262 0 L262 150 C180 110 90 150 0 140 Z" fill="var(--green-deep)"/>
      <path d="M0 250 C60 260 100 300 170 327 L0 327 Z" fill="var(--green-pale)"/>
      <path d="M262 290 C230 300 220 320 210 327 L262 327 Z" fill="var(--green-soft)"/>
    </svg>
    <p class="txt kicker c-white" style="left:14px;top:22px;">Summer is 2 Months Away!</p>
    <p class="txt title c-white" style="left:14px;top:46px;width:170px;">Join the 12-Week<br>Amber Broth<br>Quest<br><small>(with Gummies)</small></p>
    <div class="bottle" style="left:182px;top:22px;width:54px;height:104px;" role="img" aria-label="Gummies bottle"></div>
    <p class="txt date c-deep" style="left:15px;top:154px;">Begins<br>Monday May 4th</p>
    <p class="txt promo c-ink" style="left:15px;top:186px;">LOSE UP<br><b>15LBS</b> in<br>10 Days!</p>
    <div class="photo" style="left:120px;top:140px;width:136px;height:187px;" role="img" aria-label="Smiling coach pointing at the gummies bottle"></div>
  </section>

  <!-- Card 4 -->
  <section class="card" style="left:71px;top:438px;background:var(--white);">
    <svg class="bg" viewBox="0 0 262 327" aria-hidden="true">
      <path d="M0 90 C60 70 150 90 262 60 L262 327 L0 327 Z" fill="var(--green-deep)"/>
      <path d="M200 0 L262 0 L262 60 C240 60 220 40 200 0 Z" fill="var(--green-mid)"/>
      <path d="M0 280 C60 260 120 280 160 327 L0 327 Z" fill="var(--green-mid)"/>
    </svg>
    <p class="txt headline c-deep" style="left:17px;top:18px;">Get Your Summer<br>Body Ready!</p>
    <div class="bottle" style="left:204px;top:54px;width:42px;height:76px;" role="img" aria-label="Gummies bottle"></div>
    <p class="txt title c-white" style="left:21px;top:90px;width:185px;">Join the 12-Week<br>Amber Broth<br>Quest<br>on May 4<sup>th</sup>!</p>
    <p class="txt promo-caps c-soft" style="left:21px;top:194px;">LOSE UP TO<br><b>5LBS</b><br>IN 10 DAYS!</p>
    <div class="photo pink" style="left:130px;top:155px;width:122px;height:172px;" role="img" aria-label="Coach in pink outfit cheering with gummies"></div>
  </section>

  <!-- Card 5 -->
  <section class="card" style="left:358px;top:438px;">
    <svg class="bg" viewBox="0 0 262 327" aria-hidden="true">
      <path d="M0 0 L262 0 L262 40 C180 70 90 40 0 70 Z" fill="var(--green-deep)"/>
      <path d="M0 285 C60 280 90 300 130 327 L0 327 Z" fill="var(--green-deep)"/>
      <path d="M130 327 C200 300 240 300 262 300 L262 327 Z" fill="var(--green-pale)"/>
    </svg>
    <p class="txt kicker c-soft" style="left:22px;top:20px;font-size:12px;">Summer is 2 Months Away!</p>
    <p class="txt title c-green" style="left:22px;top:74px;width:170px;">Join the 12-Week<br>Amber Broth<br>Quest<br><small>(with Gummies)</small></p>
    <div class="bottle" style="left:202px;top:52px;width:40px;height:76px;" role="img" aria-label="Gummies bottle"></div>
    <p class="txt date c-ink" style="left:24px;top:174px;">Begins<br>Monday May 4th</p>
    <p class="txt promo c-green" style="left:24px;top:212px;">LOSE UP<br><b>15LBS</b> in<br>10 Days!</p>
    <div class="photo" style="left:124px;top:130px;width:134px;height:197px;" role="img" aria-label="Smiling coach pointing at the gummies bottle"></div>
  </section>

  <!-- Card 6 -->
  <section class="card" style="left:644px;top:438px;background:var(--green-pale);">
    <svg class="bg" viewBox="0 0 262 327" aria-hidden="true">
      <path d="M180 0 L262 0 L262 120 C220 90 190 60 180 0 Z" fill="var(--green-deep)"/>
      <path d="M0 210 C80 200 160 220 262 200 L262 327 L0 327 Z" fill="var(--white)"/>
      <circle cx="190" cy="270" r="66" fill="var(--green-pale)"/>
    </svg>
    <p class="txt headline c-deep" style="left:17px;top:20px;">Get Your<br>Summer<br>Body Ready!</p>
    <div class="bottle" style="left:198px;top:34px;width:48px;height:96px;" role="img" aria-label="Gummies bottle"></div>
    <p class="txt title c-green" style="left:17px;top:114px;width:175px;">Join the 12-Week<br>Amber Broth<br>Quest<br>on May 4<sup>th</sup>!</p>
    <p class="txt promo-caps c-deep" style="left:19px;top:240px;">LOSE UP TO<br><b>5LBS</b><br>IN 10 DAYS!</p>
    <div class="photo pink" style="left:132px;top:185px;width:122px;height:142px;" role="img" aria-label="Coach in pink outfit cheering with gummies"></div>
  </section>

  <!-- Card 7 -->
  <section class="card" style="left:71px;top:803px;">
    <svg class="bg" viewBox="0 0 262 327" aria-hidden="true">
      <path d="M0 235 C80 245 160 210 262 230 L262 327 L0 327 Z" fill="var(--green-deep)"/>
      <circle cx="193" cy="80" r="80" fill="var(--green-pale)"/>
    </svg>
    <div class="photo round" style="left:129px;top:16px;width:128px;height:128px;" role="img" aria-label="Smiling coach holding the gummies bottle"></div>
    <p class="txt kicker" style="left:14px;top:48px;font-size:18px;line-height:1.15;color:var(--green-soft);">Summer is<br>2 Months<br>Away!</p>
    <p class="txt title c-green" style="left:13px;top:146px;width:240px;">Join the 12-Week<br>Amber Broth<br>Quest <small>(with Gummies)</small></p>
    <p class="txt date c-white" style="left:13px;top:240px;">Begins<br>Monday May 4th</p>
    <p class="txt promo c-white" style="left:14px;top:270px;">LOSE UP <b>15LBS</b> in<br>10 Days!</p>
    <div class="bottle" style="left:198px;top:218px;width:48px;height:100px;" role="img" aria-label="Gummies bottle"></div>
  </section>

  <!-- Card 8 -->
  <section class="card" style="left:358px;top:803px;background:var(--white);">
    <svg class="bg" viewBox="0 0 262 327" aria-hidden="true">
      <path d="M0 0 L262 0 L262 20 C200 40 150 110 0 132 Z" fill="var(--green-deep)"/>
      <path d="M0 220 C50 210 90 250 110 327 L0 327 Z" fill="var(--green-pale)"/>
      <circle cx="195" cy="270" r="68" fill="var(--green-pale)"/>
    </svg>
    <p class="txt headline c-soft" style="left:17px;top:18px;">Get Your<br>Summer<br>Body<br>Ready!</p>
    <div class="bottle" style="left:190px;top:32px;width:48px;height:100px;" role="img" aria-label="Gummies bottle"></div>
    <p class="txt title c-green" style="left:15px;top:140px;width:185px;">Join the 12-Week<br>Amber Broth<br>Quest<br>on May 4<sup>th</sup>!</p>
    <p class="txt promo-caps c-green" style="left:15px;top:242px;">LOSE UP TO<br><b>5LBS</b><br>IN 10 DAYS!</p>
    <div class="photo pink" style="left:134px;top:180px;width:124px;height:147px;" role="img" aria-label="Coach in pink outfit cheering with gummies"></div>
  </section>

  <!-- Card 9 -->
  <section class="card" style="left:644px;top:803px;background:var(--white);">
    <svg class="bg" viewBox="0 0 262 327" aria-hidden="true">
      <path d="M0 0 L262 0 L262 60 C180 100 80 60 0 90 Z" fill="var(--green-deep)"/>
      <path d="M0 225 C80 200 180 210 262 205 L262 327 L0 327 Z" fill="var(--green-pale)"/>
    </svg>
    <p class="txt headline c-soft" style="left:0;top:14px;width:262px;text-align:center;">Get Your Summer<br>Body Ready!</p>
    <p class="txt title c-green" style="left:0;top:100px;width:262px;text-align:center;">Join the 12-Week<br>Amber Broth Quest<br>on May 4<sup>th</sup>!</p>
    <p class="txt promo-caps c-ink" style="left:0;top:170px;width:262px;text-align:center;font-size:9px;">LOSE UP TO <b style="font-size:13px;">5LBS</b> IN 10 DAYS!</p>
    <div class="bottle" style="left:22px;top:205px;width:52px;height:100px;" role="img" aria-label="Gummies bottle"></div>
    <div class="photo" style="left:78px;top:192px;width:88px;height:135px;" role="img" aria-label="Smiling coach pointing at the gummies"></div>
    <div class="photo pink" style="left:162px;top:188px;width:94px;height:139px;" role="img" aria-label="Coach in pink outfit cheering with gummies"></div>
  </section>

</div>
</body>
</html>
```